Mirela Dawn Business Card Design

I need a business card for my daughter. She has it all described in the file below. But it needs to be square in shape. http://www.mireladawn.example is her web site

Target Market(s)

18-35 year old women

Industry/Entity Type

Fashion

Contact Information for Business Card

Please look at the attached file as it has all the details.

Requirements
Must have
• Please look at the attached file as it has all the details.
Nice to have
Should not have

```html
<!DOCTYPE html>
<html lang="en">
<head>
<meta charset="utf-8">
<title>Mirela Dawn — Square Business Card</title>
<link rel="stylesheet" href="https://fonts.googleapis.com/css2?family=Playfair+Display:wght@700;900&family=Dancing+Script:wght@500&family=Josefin+Sans:wght@300&display=swap">
<style>
  :root {
    --page: #ffffff;
    --marble-dark: #0b0b0b;
    --marble-mid: #2a2a2a;
    --marble-light: #4a4a4a;
    --blush: #f8c4c1;
    --ink: #2b2b2b;
    --rule: #ffffff;
    --shadow: #5a5a5a;
  }
  * { box-sizing: border-box; margin: 0; padding: 0; }
  html, body { width: 1200px; height: 700px; overflow: hidden; background: var(--page); }
  .canvas { position: relative; width: 1200px; height: 700px; }

  .card {
    position: absolute;
    top: 163px;
    width: 372px;
    height: 372px;
    box-shadow: 9px 9px 0 var(--shadow);
    overflow: hidden;
  }
  .card--front { left: 171px; }
  .card--back { left: 633px; }

  .marble {
    position: absolute; inset: 0;
    background:
      radial-gradient(ellipse at 85% 90%, var(--marble-light) 0%, transparent 35%),
      radial-gradient(ellipse at 20% 15%, var(--marble-mid) 0%, transparent 45%),
      linear-gradient(135deg, var(--marble-dark) 0%, var(--marble-mid) 50%, var(--marble-dark) 100%);
  }

  .front__name {
    position: absolute; left: 0; right: 0; top: 90px;
    text-align: center;
    font-family: "Playfair Display", serif;
    font-weight: 900;
    font-size: 40px;
    letter-spacing: 2px;
    color: var(--blush);
    white-space: nowrap;
  }
  .front__rule {
    position: absolute; left: 61px; top: 169px;
    width: 254px; height: 6px;
    background: var(--rule);
  }
  .front__tagline {
    position: absolute; left: 0; right: 0; top: 205px;
    text-align: center;
    font-family: "Dancing Script", cursive;
    font-size: 34px;
    color: var(--blush);
  }

  .panel {
    position: absolute; left: 39px; top: 29px;
    width: 298px; height: 302px;
    background: var(--blush);
    color: var(--ink);
  }
  .panel__site {
    margin-top: 18px;
    text-align: center;
    font-family: "Playfair Display", serif;
    font-weight: 700;
    font-size: 26px;
    white-space: nowrap;
  }
  .panel__tagline {
    margin-top: -2px;
    text-align: center;
    font-family: "Dancing Script", cursive;
    font-size: 23px;
  }
  .contacts { list-style: none; margin-top: 16px; }
  .contact {
    display: flex; align-items: center;
    height: 46px;
    padding-left: 21px;
  }
  .contact__dot {
    width: 34px; height: 34px;
    border-radius: 50%;
    background: var(--ink);
    flex: none;
  }
  .contact__text {
    margin-left: 40px;
    font-family: "Josefin Sans", sans-serif;
    font-weight: 300;
    font-size: 14px;
    color: var(--ink);
    white-space: nowrap;
  }
</style>
</head>
<body>
<main class="canvas">
  <section class="card card--front">
    <div class="marble" role="img" aria-label="Black marble texture with white veins"></div>
    <h1 class="front__name">MIRELA DAWN</h1>
    <div class="front__rule"></div>
    <p class="front__tagline">fluent in fashion</p>
  </section>

  <section class="card card--back">
    <div class="marble" role="img" aria-label="Black marble texture with white veins"></div>
    <div class="panel">
      <p class="panel__site">mireladawn.example</p>
      <p class="panel__tagline">beauty- fashion -travel</p>
      <ul class="contacts">
        <li class="contact"><span class="contact__dot"></span><span class="contact__text">pics.example/mireladawnxo</span></li>
        <li class="contact"><span class="contact__dot"></span><span class="contact__text">chirp.example/mireladawnxo</span></li>
        <li class="contact"><span class="contact__dot"></span><span class="contact__text">@mireladawnxo</span></li>
        <li class="contact"><span class="contact__dot"></span><span class="contact__text">clips.example/mireladawn</span></li>
      </ul>
    </div>
  </section>
</main>
</body>
</html>
```